VELM VAN WRAP TO CATCH THE PUBLICS EYES!

We are looking for a van wrap design to be created for our home/business automation and alarm service company! The company has a lot of young blood! Bright and fun in sprite! Looking to provide a super new outlook on automation services and provide the best safety. This will be a van rap for a 2022 Halvard Kestrel Vantor Plus. Our style can be viewed by visiting www.homesbyvelm.com. Company phone number is 555.714.9023.

Target Market(s)

People wanting to have a alarm system for their home or business.

Industry/Entity Type

Alarm Services; Home/ Business Automation

Requirements
Must have
• Design must be for a 2022 Halvard Kestrel Vantor Plus; color and font deck sheet attached. Logo file attached.
Should not have
• Do not include any photos of Devices or phone apps. Technology changes so quickly that those items or displays become obstinate quickly

```html
<!DOCTYPE html>
<html lang="en">
<head>
<meta charset="utf-8">
<title>VELM Van Wrap</title>
<link rel="stylesheet" href="https://fonts.googleapis.com/css2?family=Montserrat:wght@300;600&family=Lato:wght@400&display=swap">
<style>
  :root {
    --bg: #ececec;
    --van-white: #ffffff;
    --van-edge: #c9c9c9;
    --wrap-grey: #a6a6a6;
    --logo-grey: #9a9a9a;
    --ink-grey: #6e6e6e;
    --brand-orange: #ee8a3c;
    --orange-tint: #f6c39a;
    --grey-tint: #c4c4c4;
    --glass: #3b3e43;
    --tyre: #1f1f1f;
    --hub: #bdbdbd;
  }
  html, body {
    margin: 0;
    padding: 0;
    width: 1126px;
    height: 1200px;
    overflow: hidden;
    background: var(--bg);
  }
  .wrap-sheet {
    display: block;
    width: 1126px;
    height: 1200px;
  }
  .van-body { fill: var(--van-white); stroke: var(--van-edge); stroke-width: 3; }
  .van-glass { fill: var(--glass); }
  .wrap-band { fill: var(--wrap-grey); }
  .wrap-arch { fill: none; stroke: var(--wrap-grey); stroke-width: 38; }
  .brand-arc { fill: none; stroke: var(--brand-orange); stroke-width: 22; }
  .dot-grey { fill: var(--grey-tint); }
  .dot-orange { fill: var(--orange-tint); }
  .tyre { fill: var(--tyre); }
  .hub { fill: var(--hub); }
  .trim { fill: var(--tyre); }
  .brand-name {
    font-family: "Montserrat", sans-serif;
    font-weight: 300;
    font-size: 130px;
    fill: var(--logo-grey);
  }
  .phone {
    font-family: "Montserrat", sans-serif;
    font-weight: 600;
    font-size: 48px;
    fill: var(--ink-grey);
  }
  .phone-dot { fill: var(--brand-orange); }
  .phone-badge { fill: var(--brand-orange); }
  .phone-glyph { fill: none; stroke: #fff; stroke-width: 3; stroke-linecap: round; }
  .web {
    font-family: "Montserrat", sans-serif;
    font-weight: 600;
    font-size: 28px;
    fill: var(--ink-grey);
  }
  .social-tag {
    font-family: "Lato", sans-serif;
    font-size: 17px;
    fill: #ffffff;
  }
  .social-dot { fill: none; stroke: #ffffff; stroke-width: 2.5; }
</style>
</head>
<body>
<svg class="wrap-sheet" viewBox="0 0 1866 1988" xmlns="http://www.w3.org/2000/svg">
  <defs>
    <g id="van-side">
      <path class="van-body" d="M360,800 L340,640 L365,420 Q380,360 430,358 L1130,368 Q1160,375 1180,400 L1310,560 Q1500,580 1600,620 Q1645,650 1650,720 L1655,800 Q1655,815 1630,820 L370,820 Z"/>
      <rect class="van-glass" x="755" y="408" width="185" height="142" rx="6"/>
      <path class="van-glass" d="M1005,418 L1150,418 L1290,572 L1010,572 Z"/>
      <path class="wrap-band" d="M340,660 Q360,575 460,570 L600,570 Q740,590 765,700 L790,800 L345,800 Z"/>
      <path class="wrap-arch" d="M1272,800 A155,155 0 0 1 1580,790"/>
      <path class="brand-arc" d="M912,360 A170,170 0 1 0 1130,578"/>
      <circle class="dot-grey" cx="682" cy="652" r="63" role="img" aria-label="Grey striped decorative disc"/>
      <circle class="dot-orange" cx="1112" cy="640" r="60" role="img" aria-label="Orange striped decorative disc"/>
      <rect class="trim" x="770" y="697" width="485" height="14" rx="7"/>
      <rect class="trim" x="942" y="590" width="26" height="56" rx="12"/>
      <rect class="trim" x="992" y="590" width="26" height="56" rx="12"/>
      <circle class="tyre" cx="520" cy="790" r="95"/>
      <circle class="hub" cx="520" cy="790" r="62"/>
      <circle class="tyre" cx="1425" cy="795" r="95"/>
      <circle class="hub" cx="1425" cy="795" r="62"/>
    </g>
    <path id="web-arc-top" d="M1255,850 A185,185 0 0 1 1575,660"/>
    <path id="web-arc-bottom" d="M288,1662 A175,175 0 0 1 604,1690"/>
  </defs>

  <!-- Passenger side -->
  <g class="van van-passenger">
    <use href="#van-side"/>
    <text class="brand-name" x="410" y="528" textLength="320" lengthAdjust="spacingAndGlyphs">VELM</text>
    <g class="social">
      <circle class="social-dot" cx="393" cy="643" r="10"/>
      <circle class="social-dot" cx="424" cy="643" r="10"/>
      <circle class="social-dot" cx="455" cy="643" r="10"/>
      <text class="social-tag" x="470" y="649">#Homesbyvelm</text>
    </g>
    <text class="web"><textPath href="#web-arc-top" startOffset="8">Homesbyvelm.com</textPath></text>
    <g class="phone-line">
      <circle class="phone-badge" cx="853" cy="760" r="18"/>
      <path class="phone-glyph" d="M846,752 Q846,768 861,769"/>
      <text class="phone" x="880" y="780">555<tspan class="phone-dot">.</tspan>714<tspan class="phone-dot">.</tspan>9023</text>
    </g>
  </g>

  <!-- Driver side -->
  <g class="van van-driver">
    <use href="#van-side" transform="translate(1865,957) scale(-1,1)"/>
    <text class="brand-name" x="1120" y="1485" textLength="320" lengthAdjust="spacingAndGlyphs">VELM</text>
    <g class="social">
      <text class="social-tag" x="1270" y="1606">#Homesbyvelm</text>
      <circle class="social-dot" cx="1410" cy="1600" r="10"/>
      <circle class="social-dot" cx="1441" cy="1600" r="10"/>
      <circle class="social-dot" cx="1472" cy="1600" r="10"/>
    </g>
    <text class="web"><textPath href="#web-arc-bottom" startOffset="40">Homesbyvelm.com</textPath></text>
    <g class="phone-line">
      <circle class="phone-badge" cx="676" cy="1717" r="18"/>
      <path class="phone-glyph" d="M669,1709 Q669,1725 684,1726"/>
      <text class="phone" x="703" y="1737">555<tspan class="phone-dot">.</tspan>714<tspan class="phone-dot">.</tspan>9023</text>
    </g>
  </g>
</svg>
</body>
</html>
```